Business Card for Orvane Parts Wholesale supplier

Hi There! I need a new business card for our company. We are specialized in selling Orvane parts, mostly we sell new LCD screens for Telvox and Slatrons. I would like to see that back in the design.

You can find the colors and logo's on our website: www.dorvak-example.nl

Industry/Entity Type

Business

Contact Information for Business Card

My Details:
Lars Vintorp

Phone: 0031612873406
E-mail: Lars@dorvak-example.nl

Slogan: "Every Part Tested Twice"

Font styles to use
Sans Serif

Colors

Designer to choose colors to be used in the design.

Requirements
Must have
• A Black backside with the Dorvak logo on it. The front side should be clean with only my contact details.
• But I'm also open for something really different or awesome!
Nice to have
• Remember that we are in the parts & repairing industry, So i'll be handing those business cards mainly to repair companies. Maybe you can do something with that thought :)

```html
<!DOCTYPE html>
<html lang="en">
<head>
<meta charset="utf-8">
<title>Dorvak Business Card</title>
<link rel="stylesheet" href="https://fonts.googleapis.com/css2?family=Open+Sans:wght@400;600;700&display=swap">
<style>
  :root {
    --backdrop: #ccd1d0;
    --card-black: #000000;
    --orange: #f07322;
    --orange-light: #f5853a;
    --white: #ffffff;
    --logo-grey: #c8c8c8;
  }
  * { box-sizing: border-box; margin: 0; padding: 0; }
  html, body {
    width: 1200px; height: 823px; overflow: hidden;
    background: var(--backdrop);
    font-family: "Open Sans", Arial, sans-serif;
  }
  .stage { position: relative; width: 1200px; height: 823px; }
  .card {
    position: absolute; width: 540px; height: 309px;
    background: var(--card-black); overflow: hidden;
    box-shadow: 0 6px 18px rgba(0,0,0,0.18);
  }
  .card--back { left: 620px; top: 120px; }
  .card--front { left: 40px; top: 390px; }

  .accent-line { position: absolute; background: var(--orange); }

  .brand { position: absolute; }
  .brand__row { display: flex; align-items: center; gap: 8px; }
  .brand__dot { border-radius: 50%; flex: none; }
  .brand__name { font-weight: 700; line-height: 1; letter-spacing: 0.5px; }
  .brand__slogan { letter-spacing: 0.6px; margin-top: 4px; white-space: nowrap; }

  .card--back .brand { left: 150px; top: 110px; }
  .card--back .brand__dot { background: var(--logo-grey); width: 22px; height: 22px; }
  .card--back .brand__name { color: var(--logo-grey); font-size: 40px; }
  .card--back .brand__slogan { color: var(--white); font-size: 10.5px; margin-left: 30px; }

  .card--front .brand { left: 290px; top: 62px; }
  .card--front .brand__dot { background: var(--orange); width: 20px; height: 20px; }
  .card--front .brand__name { color: var(--white); font-size: 36px; }
  .card--front .brand__slogan { color: var(--white); font-size: 10px; margin-left: 28px; }

  .person { position: absolute; left: 44px; top: 84px; }
  .person__name { font-size: 25px; letter-spacing: 2px; color: var(--white); font-weight: 400; line-height: 1.2; }
  .person__name .surname { color: var(--orange); }
  .person__title { font-size: 13px; letter-spacing: 1.5px; color: var(--white); }

  .contacts { list-style: none; margin-top: 12px; }
  .contacts li { display: flex; align-items: center; gap: 10px; color: var(--white); font-size: 14px; line-height: 22px; white-space: nowrap; }
  .contacts svg { width: 12px; height: 12px; fill: var(--white); flex: none; }

  .corner-shapes { position: absolute; left: 0; top: 0; }
</style>
</head>
<body>
<main class="stage">

  <section class="card card--back" aria-label="Card back">
    <div class="brand">
      <div class="brand__row"><span class="brand__dot"></span><span class="brand__name">dorvak</span></div>
      <p class="brand__slogan">Every Part Tested Twice</p>
    </div>
    <span class="accent-line" style="left:345px; top:208px; width:195px; height:5px;"></span>
  </section>

  <section class="card card--front" aria-label="Card front">
    <span class="accent-line" style="left:30px; top:0; width:5px; height:62px;"></span>
    <span class="accent-line" style="left:30px; top:222px; width:5px; height:70px;"></span>

    <div class="person">
      <h1 class="person__name">Lars <span class="surname">Vintorp</span></h1>
      <p class="person__title">MANAGER</p>
      <ul class="contacts">
        <li><svg viewBox="0 0 24 24"><path d="M6.6 10.8a15 15 0 0 0 6.6 6.6l2.2-2.2c.3-.3.7-.4 1-.2 1.1.4 2.3.6 3.6.6.6 0 1 .4 1 1V20c0 .6-.4 1-1 1A17 17 0 0 1 3 4c0-.6.4-1 1-1h3.5c.6 0 1 .4 1 1 0 1.3.2 2.5.6 3.6.1.3 0 .7-.2 1z"/></svg>0031612873406</li>
        <li><svg viewBox="0 0 24 24"><path d="M2 5h20v14H2z M2 5l10 8 10-8" stroke="#000" stroke-width="2"/></svg>Lars@dorvak-example.nl</li>
        <li><svg viewBox="0 0 24 24"><circle cx="12" cy="12" r="10"/><path d="M2 12h20M12 2c3 3 3 17 0 20M12 2c-3 3-3 17 0 20" stroke="#000" stroke-width="1.5" fill="none"/></svg>www.dorvak-example.nl</li>
      </ul>
    </div>

    <div class="brand">
      <div class="brand__row"><span class="brand__dot"></span><span class="brand__name">dorvak</span></div>
      <p class="brand__slogan">Every Part Tested Twice</p>
    </div>
    <span class="accent-line" style="left:462px; top:124px; width:78px; height:5px;"></span>

    <svg class="corner-shapes" width="540" height="309" viewBox="0 0 540 309" aria-hidden="true">
      <polygon points="300,309 362,248 421,309" fill="var(--orange-light)"/>
      <polygon points="398,286 540,154 540,309 421,309" fill="var(--orange)"/>
    </svg>
  </section>

</main>
</body>
</html>
```